Lumo Tails

im a dog walker, pet sitter and dog groomer. I can look after all pets from once a day pop in feeds of cats to small holdings and exotics. have 10 years experience in the industry. I can look after peoples dogs for the day while they are out or for longer if on holiday. I walk dogs when people are at work so the dogs get to have fun too. I do house sitting so all your animals are looked after together. you have designed my business cards and I wanted the 'lumo tails' with the paw to be the same on the leaflets. I have spoken to brandlark and they have sent a pdf file of business card and said it can be cropped. please let me know if this cant be done
im also a qualified canine hydrotherapist

Target Market(s)

pet owners

Industry/Entity Type

Pet

Requirements
Must have
• my phone number 07835204617
• email lumotails@mailnest.co.uk
• area; Tunbridge wells, Sevenoaks and surrounding areas
• I want it almost done as bullet points with the main things being the dog walking and the pet sitting.
Nice to have
• cartoon animals like business card not the cartoons with big eyes

```html
<!DOCTYPE html>
<html lang="en">
<head>
<meta charset="utf-8">
<title>Lumo Tails – Pet Care Leaflet</title>
<link rel="stylesheet" href="https://fonts.googleapis.com/css2?family=Oswald:wght@600;700&family=Lato:wght@400;700&display=swap">
<style>
  :root {
    --page-grey: #e6e7e8;
    --panel-white: #f4f5f5;
    --lime: #8fdc3c;
    --lime-light: #c9f08a;
    --grass-dark: #3f8a1f;
    --grass-mid: #6cbf2e;
    --brand-blue: #1f7fd1;
    --sky-blue: #3fc3ee;
    --violet: #5a3fd8;
    --violet-band: #7a55f0;
    --bullet-green: #8fe04a;
    --ink: #2e3236;
    --white: #ffffff;
  }
  * { margin: 0; padding: 0; box-sizing: border-box; }
  html, body { width: 1200px; height: 850px; overflow: hidden; }
  body {
    position: relative;
    background: var(--page-grey);
    font-family: "Lato", Arial, sans-serif;
  }
  .leaflet { position: absolute; inset: 0; }

  .top-strip {
    position: absolute; left: 0; top: 0; width: 1200px; height: 40px;
    background: linear-gradient(90deg, #f7f7f7, #dfe1e2);
  }
  .hero {
    position: absolute; left: 0; top: 40px; width: 1200px; height: 670px;
    background: linear-gradient(90deg, var(--lime) 0%, var(--lime-light) 40%, #b7e883 55%);
  }
  .hero-photo {
    position: absolute; left: 500px; top: 0; width: 700px; height: 670px;
    background:
      radial-gradient(ellipse at 62% 55%, #e9d3b3 0%, #d9b88d 16%, rgba(217,184,141,0) 34%),
      radial-gradient(ellipse at 88% 82%, #8c7868 0%, rgba(140,120,104,0) 18%),
      linear-gradient(180deg, var(--grass-dark) 0%, #4f9a24 35%, var(--grass-mid) 60%, #8fd04a 100%);
    -webkit-mask-image: linear-gradient(90deg, transparent 0%, #000 22%);
            mask-image: linear-gradient(90deg, transparent 0%, #000 22%);
  }

  .brand-panel {
    position: absolute; left: 40px; top: 0; width: 470px; height: 235px;
    background: linear-gradient(180deg, #ffffff, #e9eaeb);
    border-radius: 0 0 26px 26px;
    display: flex; align-items: center; justify-content: center; gap: 22px;
  }
  .brand-dot {
    width: 92px; height: 92px; border-radius: 50%;
    background: var(--sky-blue);
  }
  .brand-name {
    font-family: "Lato", Arial, sans-serif;
    font-weight: 700; font-size: 58px; line-height: 1;
    color: var(--sky-blue);
  }

  .experience { position: absolute; left: 45px; top: 285px; }
  .experience-number {
    position: absolute; left: 0; top: 0;
    font-family: "Oswald", "Arial Narrow", sans-serif;
    font-weight: 700; font-size: 150px; line-height: 1;
    color: var(--brand-blue); letter-spacing: -6px;
  }
  .experience-title {
    position: absolute; left: 148px; top: 10px; white-space: nowrap;
    font-family: "Oswald", "Arial Narrow", sans-serif;
    font-weight: 700; font-size: 62px; line-height: 1;
    color: var(--violet);
  }
  .experience-sub {
    position: absolute; left: 150px; top: 93px; white-space: nowrap;
    font-weight: 400; font-size: 37px; line-height: 1;
    color: var(--white); letter-spacing: 0.5px;
  }

  .services-band {
    position: absolute; left: 0; top: 620px; width: 1200px; height: 50px;
    background: var(--violet-band);
  }
  .services-panel {
    position: absolute; left: 48px; top: 478px; width: 575px; height: 192px;
    background: var(--violet-band);
    border-radius: 26px 26px 0 0;
  }
  .services-tab {
    position: absolute; left: 132px; top: 0; width: 286px; height: 76px;
    background: var(--lime-light);
    border-radius: 0 0 24px 24px;
    display: flex; align-items: center; justify-content: center;
    font-family: "Oswald", "Arial Narrow", sans-serif;
    font-weight: 700; font-size: 52px; color: var(--brand-blue);
  }
  .services-list {
    position: absolute; left: 30px; top: 104px;
    list-style: none;
    display: grid; grid-template-columns: 242px 300px; row-gap: 10px;
  }
  .services-list li {
    display: flex; align-items: center; gap: 10px;
    font-size: 22px; color: var(--white); line-height: 24px;
  }
  .services-list li::before {
    content: ""; width: 13px; height: 13px; border-radius: 50%;
    background: var(--bullet-green); flex: none;
  }

  .footer {
    position: absolute; left: 0; top: 710px; width: 1200px; height: 140px;
    background: linear-gradient(90deg, #ffffff 0%, #eceded 60%, #e2e3e4 100%);
  }
  .owner-name {
    position: absolute; left: 80px; top: 38px;
    font-weight: 700; font-size: 52px; line-height: 1;
    color: var(--violet-band);
  }
  .contact {
    position: absolute; right: 22px; top: 28px; text-align: right;
    color: var(--ink);
  }
  .contact-area { font-size: 29px; font-weight: 400; line-height: 1; letter-spacing: 0.2px; }
  .contact-line {
    margin-top: 14px;
    display: flex; justify-content: flex-end; align-items: center; gap: 8px;
    font-size: 29px; line-height: 1;
  }
  .contact-line svg { flex: none; }
  .contact-line .gap { width: 8px; }
</style>
</head>
<body>
<main class="leaflet">
  <div class="top-strip"></div>

  <section class="hero">
    <div class="hero-photo" role="img" aria-label="Photo of a golden retriever wearing a Santa hat sitting on grass beside a rabbit and a tabby cat"></div>
  </section>

  <header class="brand-panel">
    <span class="brand-dot" aria-hidden="true"></span>
    <span class="brand-name">Lumo Tails</span>
  </header>

  <div class="experience">
    <div class="experience-number">10</div>
    <div class="experience-title">YEARS EXPERIENCE</div>
    <div class="experience-sub">IN ANIMAL INDUSTRY</div>
  </div>

  <div class="services-band"></div>
  <section class="services-panel">
    <h2 class="services-tab">SERVICES</h2>
    <ul class="services-list">
      <li>Dog walking</li>
      <li>Dog Grooming</li>
      <li>Pet/House sitting</li>
      <li>Small holder knowledge</li>
    </ul>
  </section>

  <footer class="footer">
    <div class="owner-name">Tessa Wren</div>
    <div class="contact">
      <p class="contact-area">Tunbridge Wells, Sevenoaks and Surrounding Areas</p>
      <p class="contact-line">
        <svg width="38" height="24" viewBox="0 0 38 24" aria-hidden="true">
          <rect x="1" y="1" width="36" height="22" rx="2" fill="#3fa9e8"/>
          <path d="M2 2 L19 14 L36 2" fill="none" stroke="#ffffff" stroke-width="2"/>
        </svg>
        <span>lumotails@mailnest.co.uk</span>
        <span class="gap"></span>
        <svg width="24" height="28" viewBox="0 0 24 28" aria-hidden="true">
          <rect x="0" y="0" width="24" height="28" rx="5" fill="#3fa9e8"/>
          <path d="M8 6 C6 8 6 12 9 17 C12 22 15 23 17 22 L18 19 L15 17 L13 18 C11 16 10 14 10 12 L12 11 L11 7 Z" fill="#ffffff"/>
        </svg>
        <span>07835.204.617</span>
      </p>
    </div>
  </footer>
</main>
</body>
</html>
```